"Lemonade on Sundays" needs a cool album cover :)

We need a digital CD cover for a new comedy album called "Lemonade on Sundays" by Denise Holloway. We would like for it to have a retro/vintage feel for the artwork, inspired by the 60s & 70s. The colors should be fun and bright. We want the cover to be bright and eye-catching, and have the feel of a vinyl album cover from the 1960s/70s.
UPDATE: Since this is a digital album, and not a physical CD, we only need the artwork in a square format as it will not be printed on a CD itself. The artwork will be used to promote the album on social media, etc.
Target Market(s)
Anyone listening to comedy, Age demographic 40 and over
Industry/Entity Type
Comedy, Entertainment
Font styles to use
Other font styles liked:
- Retro fonts
Requirements
Must have
- Album Title: Lemonade on Sundays, Artist Name: Denise Holloway, Artwork or photos depicting cocktails & pajamas
Nice to have
- Vintage / Retro feel & fonts
Should not have
- Even though this is a comedy album, we do not want any comedy references on the cover such as microphones, laughing faces, etc.

```html
<!DOCTYPE html>
<html lang="en">
<head>
<meta charset="utf-8">
<title>Lemonade on Sundays — Denise Holloway</title>
<link rel="stylesheet" href="https://fonts.googleapis.com/css2?family=Caprasimo&display=swap">
<style>
  :root {
    --night: #3a0a86;
    --violet: #6a18d8;
    --deep: #24065c;
    --magenta: #f01cf0;
    --pink: #e23ae8;
    --blue: #4a2cff;
    --yellow: #ffff1a;
    --orange: #ff8a00;
    --frame: #ff3cf2;
    --photo-top: #7a1ccc;
    --photo-mid: #b03ad8;
    --photo-low: #e070e6;
  }
  html, body {
    margin: 0;
    padding: 0;
    width: 1200px;
    height: 1200px;
    overflow: hidden;
    background: var(--deep);
  }
  .album-cover {
    position: relative;
    width: 1200px;
    height: 1200px;
    overflow: hidden;
    background:
      radial-gradient(circle at 78% 30%, rgba(150, 60, 240, 0.5), transparent 45%),
      radial-gradient(circle at 20% 75%, rgba(120, 40, 220, 0.45), transparent 50%),
      radial-gradient(circle at 50% 50%, var(--violet), var(--night) 70%, var(--deep));
    font-family: "Caprasimo", "Cooper Black", serif;
  }
  .orbit-lines {
    position: absolute;
    inset: 0;
  }
  .cover-photo {
    position: absolute;
    left: 560px;
    top: 470px;
    width: 640px;
    height: 730px;
    border-radius: 320px 0 0 0;
    background:
      radial-gradient(ellipse 48% 34% at 50% 32%, rgba(200, 70, 235, 0.9), transparent 75%),
      radial-gradient(ellipse 12% 24% at 80% 52%, rgba(240, 170, 235, 0.85), transparent 80%),
      radial-gradient(ellipse 85% 26% at 60% 90%, var(--photo-low), transparent 80%),
      linear-gradient(180deg, var(--photo-top) 0%, var(--photo-mid) 60%, var(--photo-low) 100%);
    opacity: 0.95;
  }
  .frame {
    position: absolute;
    left: 28px;
    top: 28px;
    width: 1138px;
    height: 1138px;
    border: 3px solid var(--frame);
    border-radius: 4px;
  }
  .album-title {
    position: absolute;
    left: 0;
    top: 0;
    width: 1200px;
    height: 700px;
  }
  .title-face {
    fill: var(--yellow);
    stroke: var(--orange);
    stroke-width: 4;
    paint-order: stroke;
  }
  .title-depth {
    fill: var(--magenta);
  }
  .credit {
    position: absolute;
    left: 185px;
    top: 790px;
    width: 400px;
    text-align: center;
  }
  .credit-label {
    margin: 0;
    color: var(--pink);
    font-size: 30px;
    letter-spacing: 1px;
    line-height: 1;
  }
  .artist-name {
    margin: 10px 0 0;
    color: var(--yellow);
    font-size: 48px;
    line-height: 1.05;
    font-weight: 400;
  }
</style>
</head>
<body>
<main class="album-cover">
  <svg class="orbit-lines" width="1200" height="1200" viewBox="0 0 1200 1200" aria-hidden="true">
    <circle cx="1150" cy="1400" r="1020" fill="none" stroke="var(--blue)" stroke-width="6" opacity="0.8"/>
    <circle cx="1100" cy="1300" r="960" fill="none" stroke="var(--blue)" stroke-width="3" opacity="0.5"/>
    <circle cx="1050" cy="1350" r="950" fill="none" stroke="var(--magenta)" stroke-width="5" opacity="0.75"/>
    <circle cx="1000" cy="1450" r="900" fill="none" stroke="var(--blue)" stroke-width="5" opacity="0.7"/>
    <circle cx="1230" cy="1230" r="860" fill="none" stroke="var(--magenta)" stroke-width="4" opacity="0.6"/>
  </svg>

  <div class="cover-photo" role="img" aria-label="Photo of a purple cocktail in a balloon glass beside a lit candle on a small round table, tinted magenta"></div>

  <svg class="album-title" viewBox="0 0 1200 700" role="img" aria-label="Lemonade on Sundays">
    <g transform="rotate(4 400 360)" text-anchor="middle" font-family="Caprasimo, serif">
      <g class="title-depth">
        <text x="412" y="297" font-size="122">Lemonade</text>
        <text x="406" y="291" font-size="122">Lemonade</text>
        <text x="400" y="285" font-size="122">Lemonade</text>
        <text x="412" y="382" font-size="92">on</text>
        <text x="406" y="376" font-size="92">on</text>
        <text x="400" y="370" font-size="92">on</text>
        <text x="422" y="532" font-size="140">Sundays</text>
        <text x="416" y="526" font-size="140">Sundays</text>
        <text x="410" y="520" font-size="140">Sundays</text>
      </g>
      <text class="title-face" x="388" y="273" font-size="122">Lemonade</text>
      <text class="title-face" x="388" y="358" font-size="92">on</text>
      <text class="title-face" x="398" y="508" font-size="140">Sundays</text>
    </g>
  </svg>

  <section class="credit">
    <p class="credit-label">Presented by</p>
    <h2 class="artist-name">Denise<br>Holloway</h2>
  </section>

  <div class="frame" aria-hidden="true"></div>
</main>
</body>
</html>
```